Branding for salad and dip containers - retail

we are trying to modernise our packaging design
the lids will be pre-printed (only with our logo) the design can be any shape, preferably not covering the whole top as we want the product to show
NO OTHER details are needed on the lid! Just the logo in bold modern design (using our existing logo and colours) fresh modern and bold
this is the container size we use
https://www.vessorix7.co.uk/acatalog/280ml-rectangular-clear-tamperproof-container-lid.html#SID=64
see images attached of some trials made that we don’t like
1) One has too many other details
2) The other has not utilised our brand and logo

Target Market(s)

Retail Customers

Industry/Entity Type

food

Requirements
Must have
• our current existing logo included
Nice to have
• i would like to see my logo rebranded in a modern sleek design ready to printed on container tops
Should not have
• none of the current add ons- just logo bold and modern

```html
<!DOCTYPE html>
<html lang="en">
<head>
<meta charset="utf-8">
<title>Harwell's lid and side labels</title>
<link rel="stylesheet" href="https://fonts.googleapis.com/css2?family=Zilla+Slab:wght@500&family=Roboto:wght@500&display=swap">
<style>
  :root {
    --backdrop: #bde0e4;
    --brand-red: #d71a21;
    --brand-black: #000000;
    --brand-white: #ffffff;
    --guide-blue: #3a9ad9;
    --note-ink: #111111;
  }
  html, body {
    margin: 0;
    padding: 0;
    width: 1200px;
    height: 1200px;
    overflow: hidden;
    background: var(--backdrop);
  }
  .label-sheet {
    display: block;
    width: 1200px;
    height: 1200px;
  }
  .panel-black { fill: var(--brand-black); }
  .panel-red { fill: var(--brand-red); }
  .brand-disc { fill: var(--brand-red); }
  .cut-guide {
    fill: none;
    stroke: var(--guide-blue);
    stroke-width: 1.5;
  }
  .brand-name {
    font-family: "Zilla Slab", Georgia, serif;
    font-weight: 500;
    fill: var(--brand-white);
    text-anchor: middle;
  }
  .callout-line {
    fill: none;
    stroke: var(--note-ink);
    stroke-width: 6;
    stroke-linecap: round;
    stroke-linejoin: round;
  }
  .callout-text {
    font-family: "Roboto", Arial, sans-serif;
    font-weight: 500;
    font-size: 40px;
    fill: var(--note-ink);
  }
</style>
</head>
<body>
<svg class="label-sheet" viewBox="250 600 1500 1500" xmlns="http://www.w3.org/2000/svg" aria-label="Harwell's lid label and side label layouts">

  <!-- Lid label -->
  <g class="lid-label">
    <path class="panel-black" d="M298 878 H960 V1352 H900 C860 1352 850 1380 830 1410 C790 1470 720 1498 630 1498 C540 1498 470 1470 430 1410 C410 1380 400 1352 360 1352 H298 Z"/>
    <path class="panel-red" d="M298 1398 H396 C405 1398 410 1405 415 1415 C460 1490 540 1545 630 1545 C720 1545 800 1490 845 1415 C850 1405 855 1398 865 1398 H960 V1830 H298 Z"/>
    <rect class="cut-guide" x="328" y="902" width="602" height="903" rx="30"/>
    <circle class="brand-disc" cx="630" cy="1287" r="167"/>
    <text class="brand-name" x="630" y="1306" font-size="56">Harwell's</text>
    <text class="brand-name" x="630" y="1712" font-size="96">Harwell's</text>
  </g>

  <!-- Side label -->
  <g class="side-label">
    <path class="panel-black" d="M1026 1572 H1178 V1610 C1178 1625 1190 1630 1200 1640 C1222 1658 1232 1682 1232 1700 C1232 1726 1215 1756 1192 1772 C1182 1779 1178 1790 1178 1800 V1826 H1026 Z"/>
    <path class="panel-red" d="M1196 1572 H1634 V1826 H1196 V1790 C1196 1780 1210 1775 1220 1765 C1240 1745 1246 1722 1246 1700 C1246 1675 1236 1650 1216 1634 C1205 1626 1196 1620 1196 1610 Z"/>
    <rect class="cut-guide" x="1042" y="1604" width="578" height="192" rx="22"/>
    <circle class="brand-disc" cx="1152" cy="1700" r="58"/>
    <text class="brand-name" x="1152" y="1707" font-size="21">Harwell's</text>
    <text class="brand-name" x="1425" y="1722" font-size="62">Harwell's</text>
  </g>

  <!-- Callout -->
  <g class="callout">
    <path class="callout-line" d="M945 1377 L1165 1318"/>
    <path class="callout-line" d="M1107 1279 L1168 1318 L1133 1378"/>
    <path class="callout-line" d="M1185 1585 L1207 1358"/>
    <path class="callout-line" d="M1151 1401 L1208 1356 L1252 1410"/>
    <text class="callout-text" x="1200" y="1320">Clear / Transparent area</text>
  </g>
</svg>
</body>
</html>
```